IT Company based on Biology Business Needs a Business Card Design

We need a business card design for a new company called 'Lumen CELL'. We develop the machine learning solutions especially focused on deep learning algorithms for biology industry. Our initial product is a vision detection on biological images to help doctors diagnose the symptoms. We would like to see designs that use the color green.

Industry/Entity Type

Business

```html
<!DOCTYPE html>
<html lang="en">
<head>
<meta charset="utf-8">
<title>Lumen CELL — Business Card</title>
<link rel="stylesheet" href="https://fonts.googleapis.com/css2?family=Lato:ital,wght@0,400;0,700;1,400&display=swap">
<style>
  :root {
    --green: #52b044;
    --card: #f3f3f3;
    --ink: #1c1c1c;
    --white: #ffffff;
    --backdrop: #e4e6e3;
  }
  * { box-sizing: border-box; margin: 0; padding: 0; }
  html, body {
    width: 1200px; height: 800px; overflow: hidden;
    background: var(--backdrop);
    font-family: "Lato", sans-serif;
  }
  .stage {
    width: 1200px; height: 800px;
    display: flex; flex-direction: column;
    align-items: center; justify-content: center; gap: 48px;
  }
  .card {
    width: 580px; height: 330px;
    background: var(--card);
    position: relative; overflow: hidden;
    box-shadow: 0 6px 18px rgba(0,0,0,.12);
  }

  /* Front */
  .brand {
    position: absolute; top: 58px; left: 0; right: 0;
    display: flex; align-items: center; justify-content: center; gap: 14px;
  }
  .brand-dot { width: 30px; height: 30px; border-radius: 50%; background: var(--green); }
  .brand-name { font-weight: 700; font-size: 46px; color: var(--green); letter-spacing: 1px; }
  .name-band {
    position: absolute; left: 0; right: 0; top: 196px; height: 72px;
    background: var(--green); color: var(--white);
    text-align: right; padding: 10px 36px 0 0;
  }
  .person-name { font-size: 27px; letter-spacing: 1.5px; font-weight: 400; }
  .person-role { font-size: 15px; font-style: italic; letter-spacing: 1px; margin-top: 2px; }

  /* Back */
  .edge-strip { position: absolute; left: 0; top: 0; bottom: 0; width: 18px; background: var(--green); }
  .address-column { position: absolute; left: 222px; top: 0; bottom: 0; width: 176px; background: var(--green); }
  .contact {
    position: absolute; display: flex; gap: 14px; align-items: flex-start;
  }
  .contact svg { flex: none; }
  .contact-label { font-weight: 700; font-size: 17px; letter-spacing: .5px; margin-bottom: 6px; }
  .contact-line { font-size: 14px; line-height: 1.3; }
  .contact--email { left: 40px; top: 34px; color: var(--ink); }
  .contact--address { left: 236px; top: 138px; color: var(--white); }
  .contact--phone { left: 418px; top: 232px; color: var(--ink); }
</style>
</head>
<body>
<main class="stage">
  <section class="card card--front" aria-label="Card front">
    <div class="brand">
      <span class="brand-dot"></span>
      <span class="brand-name">Lumen CELL</span>
    </div>
    <div class="name-band">
      <p class="person-name">MARA ELLISON</p>
      <p class="person-role">Executive Director</p>
    </div>
  </section>

  <section class="card card--back" aria-label="Card back">
    <div class="edge-strip"></div>
    <div class="address-column"></div>

    <div class="contact contact--email">
      <svg width="40" height="34" viewBox="0 0 40 34" fill="none" stroke="#1c1c1c" stroke-width="3">
        <rect x="2" y="2" width="36" height="30" rx="2"/>
        <path d="M2 4 L20 19 L38 4"/>
      </svg>
      <div>
        <p class="contact-label">EMAIL</p>
        <p class="contact-line">info@lumencell.com</p>
        <p class="contact-line">www.lumencell.com</p>
      </div>
    </div>

    <div class="contact contact--address">
      <svg width="26" height="36" viewBox="0 0 26 36" fill="none" stroke="#ffffff" stroke-width="2.5">
        <path d="M13 34 C4 22 2 17 2 12 A11 11 0 0 1 24 12 C24 17 22 22 13 34 Z"/>
        <circle cx="13" cy="12" r="4"/>
      </svg>
      <div>
        <p class="contact-label">ADDRESS</p>
        <p class="contact-line">Address Line 1</p>
        <p class="contact-line">Address Line 2</p>
      </div>
    </div>

    <div class="contact contact--phone">
      <svg width="26" height="40" viewBox="0 0 26 40" fill="none" stroke="#1c1c1c" stroke-width="3">
        <rect x="2" y="2" width="22" height="36" rx="3"/>
        <line x1="2" y1="8" x2="24" y2="8"/>
        <line x1="2" y1="31" x2="24" y2="31"/>
      </svg>
      <div>
        <p class="contact-label">PHONE</p>
        <p class="contact-line">(1) 555 210 384</p>
        <p class="contact-line">(1) 555 210 384</p>
      </div>
    </div>
  </section>
</main>
</body>
</html>
```